KV MOTORS BANNER/SIGN DESIGN

Design a banner sign for outdoor use for KV MOTORS - a premium pre owned vehicle sales center. The size must be 36 feet in width
and 3 feet in height.

Information required: logo (attached)
-PREMIUM PRE-OWEND VEHICLE SALES
- 403.555.0172

perhaps in smaller font: BUY-SELL-TRADE

prefer white background but could possibly do red matching the logo

```html
<!DOCTYPE html>
<html lang="en">
<head>
<meta charset="utf-8">
<title>KV Motors Banner</title>
<link rel="stylesheet" href="https://fonts.googleapis.com/css2?family=PT+Sans:wght@700&family=Nunito+Sans:wght@800&display=swap">
<style>
  :root {
    --stage: #9c9d9c;
    --paper: #ffffff;
    --brand-red: #e21d25;
    --ink: #2b2a29;
  }
  * { margin: 0; padding: 0; box-sizing: border-box; }
  html, body { width: 1200px; height: 385px; overflow: hidden; background: var(--stage); }
  .stage { position: relative; width: 1200px; height: 385px; }

  .banner {
    position: absolute; left: 39px; width: 1122px; height: 93px;
    background: var(--paper);
    box-shadow: 3px 4px 6px rgba(0,0,0,0.35);
  }
  .banner--red { top: 79px; }
  .banner--white { top: 218px; }

  .banner__panel {
    position: absolute; left: 477px; top: 0; width: 645px; height: 93px;
    background: var(--brand-red);
  }

  .brand-mark {
    position: absolute; left: 13px; top: 6px; width: 82px; height: 82px;
    border: 5px solid var(--brand-red); border-radius: 50%;
  }
  .divider {
    position: absolute; top: 14px; width: 2px; height: 65px; background: var(--ink);
  }
  .divider--brand { left: 107px; }
  .divider--message { left: 475px; }

  .brand-name {
    position: absolute; left: 122px; top: 2px;
    font: 700 56px/1 "PT Sans", sans-serif;
    color: var(--ink); letter-spacing: 5px; white-space: nowrap;
  }
  .tagline {
    position: absolute; left: 122px; top: 59px;
    font: 700 23px/1 "PT Sans", sans-serif;
    color: var(--brand-red); letter-spacing: 13px; white-space: nowrap;
  }

  .headline {
    position: absolute; left: 491px; top: 5px; width: 614px;
    font: 700 34px/1 "PT Sans", sans-serif;
    letter-spacing: 1px;
    color: var(--ink); white-space: nowrap; text-align: center;
  }

  .phone {
    position: absolute; left: 648px; top: 43px; width: 301px;
    font: 800 43px/1 "Nunito Sans", sans-serif;
    text-align: center; letter-spacing: 0.5px; white-space: nowrap;
  }
  .banner--red .phone { color: var(--paper); }
  .banner--white .phone { color: var(--brand-red); }

  .arrows { position: absolute; top: 52px; width: 135px; height: 30px; }
  .arrows--in-left { left: 492px; }
  .arrows--in-right { left: 970px; }
  .arrows path { fill: var(--ink); }
</style>
</head>
<body>
<div class="stage">

  <section class="banner banner--red" aria-label="KV Motors banner, red version">
    <div class="banner__panel"></div>
    <div class="brand-mark"></div>
    <div class="divider divider--brand"></div>
    <div class="brand-name">KV MOTORS</div>
    <div class="tagline">BUY-SELL-TRADE</div>
    <div class="headline">PREMIUM PRE-OWEND VEHICLE SALES</div>
    <svg class="arrows arrows--in-left" viewBox="0 0 135 30" aria-hidden="true">
      <path d="M0 0L15 15L0 30Z M30 0L45 15L30 30Z M60 0L75 15L60 30Z M90 0L105 15L90 30Z M120 0L135 15L120 30Z"/>
    </svg>
    <div class="phone">403.555.0172</div>
    <svg class="arrows arrows--in-right" viewBox="0 0 135 30" aria-hidden="true">
      <path d="M15 0L0 15L15 30Z M45 0L30 15L45 30Z M75 0L60 15L75 30Z M105 0L90 15L105 30Z M135 0L120 15L135 30Z"/>
    </svg>
  </section>

  <section class="banner banner--white" aria-label="KV Motors banner, white version">
    <div class="brand-mark"></div>
    <div class="divider divider--brand"></div>
    <div class="brand-name">KV MOTORS</div>
    <div class="tagline">BUY-SELL-TRADE</div>
    <div class="divider divider--message"></div>
    <div class="headline">PREMIUM PRE-OWEND VEHICLE SALES</div>
    <svg class="arrows arrows--in-left" viewBox="0 0 135 30" aria-hidden="true">
      <path d="M0 0L15 15L0 30Z M30 0L45 15L30 30Z M60 0L75 15L60 30Z M90 0L105 15L90 30Z M120 0L135 15L120 30Z"/>
    </svg>
    <div class="phone">403.555.0172</div>
    <svg class="arrows arrows--in-right" viewBox="0 0 135 30" aria-hidden="true">
      <path d="M15 0L0 15L15 30Z M45 0L30 15L45 30Z M75 0L60 15L75 30Z M105 0L90 15L105 30Z M135 0L120 15L135 30Z"/>
    </svg>
  </section>

</div>
</body>
</html>
```